Pelverhook LLC
Business Cards & Stationary
Professional
Tobias Wendell
President
482 Orchard Crest Road
Dunmore Falls, NJ 07934-2718
tobias.wendell@mailvexo.com
www.pelverhook.com
I require the full suite of stationary products i.e.:- Business card, letterhead, envelope, fax cover sheet, thank you cards, invoice etc.
Just the logo on the back of the card.

```html
<!DOCTYPE html>
<html lang="en">
<head>
<meta charset="utf-8">
<title>Pelverhook LLC – Business Card</title>
<link href="https://fonts.googleapis.com/css2?family=PT+Sans:wght@400;700&display=swap" rel="stylesheet">
<style>
  :root {
    --page-bg: #ece8e2;
    --card-white: #ffffff;
    --brand-blue: #1c5ba8;
    --band-top: #3f82cc;
    --band-bottom: #1a4f95;
    --tagline-grey: #6b6f75;
    --rule-light: rgba(255,255,255,0.75);
    --text-white: #ffffff;
  }
  * { margin: 0; padding: 0; box-sizing: border-box; }
  html, body {
    width: 1200px; height: 780px; overflow: hidden;
    background: var(--page-bg);
    font-family: "PT Sans", Arial, sans-serif;
  }
  .canvas {
    width: 1200px; height: 780px;
    display: flex; align-items: center; justify-content: center;
  }
  .business-card {
    position: relative;
    width: 1050px; height: 600px;
    background: var(--card-white);
    border-radius: 36px;
    overflow: hidden;
    box-shadow: 0 6px 22px rgba(0,0,0,0.18);
  }
  .brand {
    position: absolute; top: 48px; left: 0; right: 0;
    display: flex; flex-direction: column; align-items: center;
  }
  .brand-dot {
    width: 118px; height: 118px; border-radius: 50%;
    background: var(--brand-blue);
    margin-bottom: 22px;
  }
  .brand-name {
    font-weight: 700; font-size: 74px; line-height: 1;
    letter-spacing: 2px; color: var(--brand-blue);
    text-transform: uppercase;
  }
  .brand-tagline {
    margin-top: 14px;
    font-size: 21px; letter-spacing: 4px;
    color: var(--tagline-grey); text-transform: uppercase;
  }
  .info-band {
    position: absolute; left: 0; right: 0; bottom: 0; height: 232px;
    background: linear-gradient(180deg, var(--band-top) 0%, var(--band-bottom) 100%);
    border-top: 4px solid var(--brand-blue);
    display: flex; align-items: center; justify-content: center;
    color: var(--text-white);
  }
  .person {
    width: 50%; padding-right: 34px; text-align: right;
  }
  .person-name { font-weight: 700; font-size: 34px; line-height: 1.15; }
  .person-title { font-weight: 700; font-size: 25px; line-height: 1.3; margin-bottom: 14px; }
  .person-address { font-size: 24px; line-height: 1.3; }
  .divider {
    width: 2px; height: 168px; background: var(--rule-light);
  }
  .contact-list {
    width: 50%; padding-left: 34px; list-style: none;
  }
  .contact-item {
    display: flex; align-items: center; gap: 16px;
    font-size: 24px; line-height: 1.5;
  }
  .contact-item svg { width: 22px; height: 22px; flex: none; fill: var(--text-white); }
</style>
</head>
<body>
<main class="canvas">
  <article class="business-card">
    <header class="brand">
      <div class="brand-dot"></div>
      <div class="brand-name">Pelverhook LLC</div>
      <div class="brand-tagline">Consulting · Investments · Advisers</div>
    </header>

    <section class="info-band">
      <div class="person">
        <div class="person-name">Tobias Wendell</div>
        <div class="person-title">President</div>
        <div class="person-address">482 Orchard Crest Road<br>Dunmore Falls, NJ 07934-2718</div>
      </div>
      <div class="divider"></div>
      <ul class="contact-list">
        <li class="contact-item">
          <svg viewBox="0 0 24 24" aria-hidden="true"><path d="M6.6 10.8a15.1 15.1 0 0 0 6.6 6.6l2.2-2.2c.3-.3.7-.4 1-.2 1.1.4 2.3.6 3.6.6.6 0 1 .4 1 1V20c0 .6-.4 1-1 1A17 17 0 0 1 3 4c0-.6.4-1 1-1h3.5c.6 0 1 .4 1 1 0 1.3.2 2.5.6 3.6.1.3 0 .7-.2 1z"/></svg>
          201.555.0148
        </li>
        <li class="contact-item">
          <svg viewBox="0 0 24 24" aria-hidden="true"><path d="M7 1h10a2 2 0 0 1 2 2v18a2 2 0 0 1-2 2H7a2 2 0 0 1-2-2V3a2 2 0 0 1 2-2zm0 3v14h10V4zm5 15.2a1.2 1.2 0 1 0 0 2.4 1.2 1.2 0 0 0 0-2.4z"/></svg>
          201.555.0192
        </li>
        <li class="contact-item">
          <svg viewBox="0 0 24 24" aria-hidden="true"><path d="M6 2h9l3 3v5h2a2 2 0 0 1 2 2v8a2 2 0 0 1-2 2H4a2 2 0 0 1-2-2v-8a2 2 0 0 1 2-2h2zm2 2v6h8V6h-2V4zm-2 10v2h3v-2zm5 0v2h3v-2zm5 0v2h3v-2z"/></svg>
          201.555.0148
        </li>
        <li class="contact-item">
          <svg viewBox="0 0 24 24" aria-hidden="true"><path d="M2 5h20v14H2zm2 2v.5l8 5.5 8-5.5V7zm0 2.9V17h16V9.9l-8 5.5z"/></svg>
          tobias.wendell@mailvexo.com
        </li>
      </ul>
    </section>
  </article>
</main>
</body>
</html>
```